Professional IT Company Letterhead

We need a new letterhead design to incorporate our new login and business card design recently received here on Sketch Guild. We want the same look and feel as the other two accepted projects. We want a professional and clean design.

Target Market(s)

Medical/Dental and Professional Services Businesses (CPA, Attorney, Architect etc)

Industry/Entity Type

Business

Requirements
Must have
• Clean and professional, consistent brand with our current design of our new logo and business cards.
Nice to have
• Would like to also be able to use the design on our newsletter header

```html
<!DOCTYPE html>
<html lang="en">
<head>
<meta charset="utf-8">
<title>Tidewell Technology Letterhead</title>
<link href="https://fonts.googleapis.com/css2?family=Quicksand:wght@500;600&family=Mulish:wght@400&display=swap" rel="stylesheet">
<style>
  :root {
    --backdrop: #cccccc;
    --paper: #fafafa;
    --brand-blue: #1f9ad6;
    --deep-blue: #1573b8;
    --ink: #1b2a3a;
    --water-top: #ffffff;
    --water-bottom: #a9cdea;
    --watermark: #eef4f9;
  }
  html, body {
    margin: 0;
    padding: 0;
    width: 1200px;
    height: 1200px;
    overflow: hidden;
    background: var(--backdrop);
  }
  .letterhead {
    position: absolute;
    left: 204px;
    top: 40px;
    width: 792px;
    height: 1120px;
    background: var(--paper);
    overflow: hidden;
  }
  .brand {
    position: absolute;
    top: 64px;
    left: 0;
    width: 100%;
    text-align: center;
    color: var(--brand-blue);
  }
  .brand-name {
    display: inline-flex;
    align-items: center;
    gap: 12px;
    font-family: "Quicksand", sans-serif;
    font-weight: 600;
    font-size: 40px;
    line-height: 1;
    color: var(--brand-blue);
  }
  .brand-dot {
    width: 30px;
    height: 30px;
    border-radius: 50%;
    background: var(--brand-blue);
  }
  .brand-tagline {
    margin-top: 8px;
    font-family: "Quicksand", sans-serif;
    font-weight: 500;
    font-size: 11px;
    letter-spacing: 1px;
    color: var(--brand-blue);
  }
  .watermark-area {
    position: absolute;
    left: 8px;
    top: 356px;
    width: 596px;
    height: 420px;
    border-radius: 48% 52% 40% 60% / 50% 45% 55% 50%;
    background: radial-gradient(ellipse at 65% 50%, var(--watermark) 0%, rgba(238,244,249,0.4) 60%, rgba(250,250,250,0) 100%);
  }
  .water-band {
    position: absolute;
    left: 0;
    bottom: 0;
    width: 100%;
    height: 120px;
    background: linear-gradient(to bottom, var(--water-top) 0%, var(--water-bottom) 100%);
  }
  .water-surface {
    position: absolute;
    left: 0;
    bottom: 106px;
    width: 100%;
    height: 20px;
  }
  .contact {
    position: absolute;
    left: 0;
    bottom: 40px;
    width: 100%;
    text-align: center;
    font-family: "Mulish", sans-serif;
    font-size: 14px;
    line-height: 19px;
    color: var(--ink);
  }
  .contact-line { display: flex; justify-content: center; align-items: center; gap: 6px; }
  .contact-icon { width: 12px; height: 12px; fill: var(--deep-blue); }
</style>
</head>
<body>
  <main class="letterhead">
    <header class="brand">
      <div class="brand-name"><span class="brand-dot"></span>Tidewell Technology</div>
      <div class="brand-tagline">IT Support for Medical &amp; Dental Practices</div>
    </header>

    <div class="watermark-area" role="img" aria-label="Faint brand mascot watermark"></div>

    <div class="water-band" role="img" aria-label="Water splash band along the footer"></div>
    <svg class="water-surface" viewBox="0 0 792 20" preserveAspectRatio="none" aria-hidden="true">
      <path d="M0 12 Q 40 4 80 12 T 160 12 T 240 12 T 320 12 T 400 12 T 480 12 T 560 12 T 640 12 T 720 12 T 792 10 L792 20 L0 20 Z" fill="#5aa7dc" opacity="0.55"/>
      <path d="M0 13 Q 40 7 80 13 T 160 13 T 240 13 T 320 13 T 400 13 T 480 13 T 560 13 T 640 13 T 720 13 T 792 11" fill="none" stroke="#1573b8" stroke-width="2"/>
    </svg>

    <footer class="contact">
      <div class="contact-line">
        <svg class="contact-icon" viewBox="0 0 12 12"><path d="M1 4 Q6 0 11 4 L9 6 L8 4 H4 L3 6 Z M3 7 H9 L10 11 H2 Z"/></svg>
        <span>+00 111 222 3333</span>
        <svg class="contact-icon" viewBox="0 0 12 12"><path d="M1 3 H11 V10 H1 Z" /><path d="M1 3 L6 7 L11 3" fill="none" stroke="#fff" stroke-width="1"/></svg>
        <span>yourname@yourwebsite.com</span>
        <svg class="contact-icon" viewBox="0 0 12 12"><circle cx="6" cy="6" r="5"/><path d="M1 6 H11 M6 1 V11 M6 1 Q2 6 6 11 M6 1 Q10 6 6 11" fill="none" stroke="#fff" stroke-width="0.8"/></svg>
        <span>www.yourwebsite.com</span>
      </div>
      <div>Your Long Commercial or business address in 2 line</div>
    </footer>
  </main>
</body>
</html>
```